Business card revamp

we are refrigeration mechanic i need a modern professional double side business card using my current branding
The card information must have site address~ 17 Whitlow st tallowmere, Vic 3752 postal address~ P.o. Box 862 tallowmere,Vic 3751 Phone Number~0358149637 Fax Nunber~0358260518 Email address~ brucet@pelvanor.com.au Title~ Manager Licence numbers~ AU47391, NSW 681329K Web site~ www.frostrimvane.com.au

Industry/Entity Type

Business

```html
<!DOCTYPE html>
<html lang="en">
<head>
<meta charset="utf-8">
<title>Frostrimvane Business Card</title>
<link rel="stylesheet" href="https://fonts.googleapis.com/css2?family=Questrial&family=Mulish:wght@700&display=swap">
<style>
  :root {
    --backdrop: #e6e6e6;
    --card: #2a2a2c;
    --card-dark: #1f1f21;
    --heat-red: #c8323a;
    --cool-blue: #1f78c4;
    --text-light: #e8e8e8;
    --text-grey: #b4b4b4;
    --logo-grey: #bdbdbd;
  }
  * { box-sizing: border-box; margin: 0; padding: 0; }
  html, body { width: 1200px; height: 720px; overflow: hidden; }
  body {
    background: var(--backdrop);
    font-family: "Questrial", "Century Gothic", sans-serif;
    position: relative;
  }
  .card {
    position: absolute;
    top: 205px;
    width: 540px;
    height: 310px;
    background: linear-gradient(160deg, var(--card) 0%, var(--card-dark) 100%);
    overflow: hidden;
  }
  .card--front { left: 40px; }
  .card--back { left: 620px; }
  .wave-band {
    position: absolute;
    left: 0;
    width: 540px;
    height: 120px;
  }
  .card--front .wave-band { top: 90px; }
  .card--back .wave-band { top: 95px; }

  .brand-name {
    color: var(--logo-grey);
    letter-spacing: 0.05em;
    white-space: nowrap;
  }
  .tagline {
    color: var(--text-light);
    letter-spacing: 0.16em;
    text-transform: uppercase;
    white-space: nowrap;
  }
  .card--front .brand {
    position: absolute;
    top: 116px;
    left: 0;
    width: 540px;
    text-align: center;
  }
  .card--front .brand-name { font-size: 56px; line-height: 1; }
  .card--front .tagline { font-size: 14px; margin-top: 8px; }
  .web {
    position: absolute;
    top: 268px;
    width: 540px;
    text-align: center;
    font-size: 17px;
    color: var(--text-light);
  }

  .card--back .brand { position: absolute; top: 42px; left: 16px; }
  .card--back .brand-name { font-size: 30px; line-height: 1; }
  .card--back .tagline { font-size: 7px; margin-top: 4px; margin-left: 36px; }

  .licence {
    position: absolute;
    top: 116px;
    left: 15px;
    font-size: 14px;
    line-height: 19px;
    color: var(--text-grey);
    font-weight: bold;
  }
  .holder {
    position: absolute;
    top: 134px;
    right: 16px;
    text-align: right;
  }
  .holder-name {
    font-family: "Mulish", "Century Gothic", sans-serif;
    font-weight: 700;
    font-size: 20px;
    color: var(--cool-blue);
  }
  .holder-title { font-size: 16px; color: var(--text-light); margin-top: 4px; }

  .contact {
    position: absolute;
    left: 15px;
    font-size: 14px;
    line-height: 19px;
    color: var(--text-light);
    white-space: nowrap;
  }
  .contact .label { color: var(--heat-red); }
  .contact--phone { top: 162px; }
  .contact--email { top: 210px; }
  .contact--address { top: 242px; left: 17px; line-height: 20px; }
</style>
</head>
<body>
  <section class="card card--front">
    <svg class="wave-band" role="img" aria-label="Faint intertwined wave ribbons behind the brand name" viewBox="0 0 540 120" preserveAspectRatio="none">
      <defs>
        <linearGradient id="waveFadeFront" x1="0" x2="1" y1="0" y2="0">
          <stop offset="0" stop-color="#ffffff" stop-opacity="0"/>
          <stop offset="0.5" stop-color="#ffffff" stop-opacity="0.06"/>
          <stop offset="1" stop-color="#ffffff" stop-opacity="0.02"/>
        </linearGradient>
      </defs>
      <rect x="0" y="10" width="540" height="100" rx="50" fill="url(#waveFadeFront)"/>
    </svg>
    <div class="brand">
      <div class="brand-name">FROSTRIMVANE</div>
      <div class="tagline">Heating and Cooling Specialists</div>
    </div>
    <div class="web">frostrimvane.com.au</div>
  </section>

  <section class="card card--back">
    <svg class="wave-band" role="img" aria-label="Faint intertwined wave ribbons across the card" viewBox="0 0 540 120" preserveAspectRatio="none">
      <defs>
        <linearGradient id="waveFadeBack" x1="0" x2="1" y1="0" y2="0">
          <stop offset="0" stop-color="#ffffff" stop-opacity="0"/>
          <stop offset="0.5" stop-color="#ffffff" stop-opacity="0.06"/>
          <stop offset="1" stop-color="#ffffff" stop-opacity="0.02"/>
        </linearGradient>
      </defs>
      <rect x="0" y="10" width="540" height="100" rx="50" fill="url(#waveFadeBack)"/>
    </svg>
    <div class="brand">
      <div class="brand-name">FROSTRIMVANE</div>
      <div class="tagline">Heating and Cooling Specialists</div>
    </div>

    <div class="licence">
      <div>Licence # AU47391</div>
      <div>NSW 681329K</div>
    </div>

    <div class="holder">
      <div class="holder-name">Bruce Tarrant</div>
      <div class="holder-title">Manager</div>
    </div>

    <div class="contact contact--phone">
      <div><span class="label">Ph:</span> 035.814.9637</div>
      <div><span class="label">Fax:</span> 03.582.60518</div>
    </div>
    <div class="contact contact--email">
      <span class="label">Email:</span> brucet@pelvanor.com.au
    </div>
    <div class="contact contact--address">
      <div><span class="label">Postal Address:</span> P.o. Box 862 tallowmere,Vic 3751</div>
      <div><span class="label">Site Address:</span> 17 Whitlow st tallowmere, Vic 3752</div>
    </div>
  </section>
</body>
</html>
```